Tallymint - A/B testing for professionals

We need to improve the presentation layer (design only) of our tool tallymint.example.

www.tallymint.example is a A/B testing tool for websites and all kind of applications. The most important features are already listed on our actual webpage and the attached screenshots.
the animated icons on the front page should be included into the design and should match the color scheme. if you think you need to add a logo or similar things to it - feel free to offer us good proposals. you can reach us by sending us a mail to: support@tallymint.example

our needs listed:
-we'd rather have a very good improvement of the actual design instead of a big redesign with all colours changed etc.
- the pages in the screenshots attached should be redesigned. The amount of different layouts will be around 2 - 4 depending on the design.
- the animated icons on www.tallyrmint.example must be included into the design.
- the colors should match with the animated icons.
- we won't need any code. Psd / ai / graphic files only.

Target Market(s)

everyone who sells something with their webpage / application.

Number of Pages Required

3 page

Colors
85cae6
3276b5
85abd2
cee9f5
eaf1f7
0455a3
000000
0492cd

Requirements
Must have
• - animated icons included on the main page.
• - color match with the animated icons on our website or good proposal for adjusting them accordingly.
• - touch of that is highly scaleable and adjustable: we invented a new query language for the project
• - sweetness of the modern web projects and libraries
• - touch that the date are not shared between different users - high value on privacy
Nice to have
• - proposal for a matching logo or including the actual properly
Should not have
• - images people in the design
• - coded versions

```html
<!DOCTYPE html>
<html lang="en">
<head>
<meta charset="utf-8">
<title>Tallymint – A/B testing made for professionals</title>
<link href="https://fonts.googleapis.com/css2?family=Open+Sans:wght@300;400;600;700&display=swap" rel="stylesheet">
<style>
  :root{
    --teal-light:#2ad2d0;
    --teal:#12b9c2;
    --teal-deep:#06788a;
    --accent:#4fbfcf;
    --icon:#5cc3d2;
    --text:#6b6b6b;
    --heading:#5e5e5e;
    --white:#ffffff;
    --paper:#f8f8f8;
    --footer:#333333;
    --footer-text:#d8d8d8;
    --pink:#f08c96;
    --sky:#b6dde9;
  }
  *{box-sizing:border-box;margin:0;padding:0}
  html,body{width:1118px;height:1200px;overflow:hidden}
  body{font-family:"Open Sans",Arial,sans-serif;color:var(--text);background:var(--white);font-weight:300}
  .wrap{position:relative;width:716px;margin:0 auto;height:100%}

  /* Hero */
  .hero{height:296px;background:radial-gradient(ellipse 70% 90% at 45% 5%,var(--teal-light) 0%,var(--teal) 45%,var(--teal-deep) 100%);color:var(--white)}
  .brand{position:absolute;left:0;top:9px;font-size:15px;font-weight:700;letter-spacing:2px;text-transform:uppercase}
  .top-nav{position:absolute;right:0;top:6px;display:flex;align-items:center;gap:10px;font-size:9px;font-weight:600;letter-spacing:.5px}
  .btn{display:inline-block;border:1.5px solid var(--white);border-radius:5px;color:var(--white);text-decoration:none}
  .top-nav .btn{padding:5px 13px}
  .top-nav a{color:var(--white);text-decoration:none}
  .hero-title{position:absolute;left:0;right:0;top:106px;text-align:center;font-size:18px;font-weight:400;letter-spacing:1.3px}
  .hero-sub{position:absolute;left:0;right:0;top:155px;text-align:center;font-size:11px;font-weight:400;letter-spacing:.6px}
  .hero-cta{position:absolute;left:50%;top:179px;transform:translateX(-50%);padding:4px 13px;font-size:9px;font-weight:600;letter-spacing:.4px;white-space:nowrap}

  /* Features */
  .features{height:364px}
  .feature{position:absolute;width:240px}
  .feature-icon{position:absolute;width:58px;height:58px}
  .feature h2,.story h2{font-size:18px;font-weight:300;letter-spacing:1.6px;color:var(--heading);text-transform:uppercase;line-height:20px}
  .feature p{font-size:10.5px;line-height:14px;letter-spacing:.5px;text-align:justify}
  .feature p b,.story b{font-weight:700;color:#555}

  /* Stories */
  .stories{height:439px;background:var(--paper)}
  .story{position:absolute}
  .story p{font-size:10.5px;line-height:14px;letter-spacing:.5px}
  .story a{color:var(--accent);text-decoration:none}
  .illustration{position:absolute;border-radius:50% 50% 50% 50% / 40% 40% 60% 60%}

  /* Footer */
  .footer{height:101px;background:var(--footer);color:var(--footer-text)}
  .footer .brand{top:12px;font-size:10px;letter-spacing:1px;color:var(--white)}
  .footer-col{position:absolute;top:35px;font-size:6.5px;line-height:14px;letter-spacing:.2px}
  .footer-col h3{font-size:6.5px;font-weight:700;color:var(--white);text-transform:uppercase}
  .social{position:absolute;right:0;top:13px;display:flex;gap:5px}
  .social span{width:11px;height:11px;border:1px solid var(--footer-text);border-radius:50%}
  .copyright{position:absolute;right:0;top:75px;font-size:6.5px;text-transform:uppercase;letter-spacing:.3px}
</style>
</head>
<body>

<header class="hero">
  <div class="wrap">
    <div class="brand">Tallymint</div>
    <nav class="top-nav">
      <a href="#">INSTALL</a>
      <a class="btn" href="#">LOGIN</a>
    </nav>
    <h1 class="hero-title">A/B testing made for professionals.</h1>
    <p class="hero-sub">Start improving your conversion rate.</p>
    <a class="btn hero-cta" href="#">INSTALL &nbsp;&nbsp;| CONFIGURE</a>
  </div>
</header>

<section class="features">
  <div class="wrap">
    <svg class="feature-icon" style="left:12px;top:38px" viewBox="0 0 58 58" fill="none" stroke="var(--icon)" stroke-width="2.2" stroke-linejoin="round">
      <circle cx="31" cy="6" r="4"/><circle cx="20" cy="8" r="1.5"/>
      <path d="M23 16h14M26 16v12L15 50h30L34 28V16"/><path d="M19 42h22"/>
    </svg>
    <div class="feature" style="left:91px;top:33px">
      <h2>Create experiments</h2>
      <p>Use the editor to create experiments by changing texts, attributes and styling. Write JavaScript, or do server side experiments.</p>
    </div>

    <svg class="feature-icon" style="left:390px;top:34px" viewBox="0 0 58 58" fill="none" stroke="var(--icon)" stroke-width="2.2" stroke-linejoin="round">
      <path d="M30 6h20v20L24 52 4 32z"/><circle cx="42" cy="14" r="3"/>
    </svg>
    <div class="feature" style="left:476px;top:33px">
      <h2>Tags</h2>
      <p>By tagging your experiments into categories and strategies, you will be able to measure how well the whole improvement strategy works.</p>
    </div>

    <svg class="feature-icon" style="left:8px;top:155px" viewBox="0 0 58 58" fill="none" stroke="var(--icon)" stroke-width="2.2">
      <path d="M3 29C16 16 42 16 55 29 42 42 16 42 3 29z"/><circle cx="29" cy="29" r="9"/><path d="M30 24a5 5 0 0 1 5 5"/>
    </svg>
    <div class="feature" style="left:91px;top:153px">
      <h2>Preview</h2>
      <p>All users can freely turn on their previewed experiments, which will be visible on the product just like any other user would see it.</p>
    </div>

    <svg class="feature-icon" style="left:394px;top:154px" viewBox="0 0 58 58" fill="none" stroke="var(--icon)" stroke-width="2.2" stroke-linejoin="round">
      <path d="M4 16h36v34H4zM4 27h36M4 38h36M16 16v34M28 16v34"/>
      <path d="M38 4h12v12H38z" fill="var(--white)"/><path d="M18 12l10-3 3 10-10 3z" fill="var(--white)"/>
    </svg>
    <div class="feature" style="left:476px;top:153px">
      <h2>Fields</h2>
      <p>Any tracking, goals, events or values can be stored in a data field, which will be automatically available in your reports.</p>
    </div>

    <svg class="feature-icon" style="left:10px;top:270px" viewBox="0 0 58 58" fill="none" stroke="var(--icon)" stroke-width="2" stroke-linejoin="round">
      <path d="M6 4h36v50H6z"/><path d="M42 10h6v44H8"/>
      <path d="M11 10h26v10H11z"/><path d="M11 25h12M11 29h12M11 33h12M27 25h10M27 29h10M27 33h10M11 40h10v8H11zM25 40h12M25 44h12M25 48h12"/>
    </svg>
    <div class="feature" style="left:91px;top:272px">
      <h2>Reports</h2>
      <p style="text-align:left">Use our standard reports or create custom reports with widgets using our query language <b>DQL</b>.</p>
    </div>

    <svg class="feature-icon" style="left:394px;top:275px" viewBox="0 0 58 58" fill="none" stroke="var(--icon)" stroke-width="2.2" stroke-linejoin="round">
      <path d="M4 30L54 8 38 50 26 34z"/><path d="M54 8L26 34v14l6-8"/>
    </svg>
    <div class="feature" style="left:476px;top:270px">
      <h2>Queries</h2>
      <p>Write your own queries. you're able to select all the data which we save and you can use them in the way ou need them.</p>
    </div>
  </div>
</section>

<section class="stories">
  <div class="wrap">
    <div class="illustration" role="img" aria-label="Illustration of a small pink house on a round island with a tree" style="left:15px;top:33px;width:170px;height:130px;background:linear-gradient(180deg,#f7a9a4 0%,#f5c9a8 55%,var(--sky) 80%)"></div>
    <div class="story" style="left:224px;top:56px;width:480px">
      <h2>Create experiments directly on the webproduct</h2>
      <p>The installation of Tallymint enables a keyboard shortcut <a href="#">CTRL + ALT + E</a> on the website. Using this shortcut it is easily possible to create lots of experiments. As long as logged in on Tallymint this shortcut will open the editor and it will assist for special desires.</p>
    </div>

    <div class="story" style="left:-1px;top:188px;width:490px">
      <h2>Check results with available reports</h2>
      <p>There are <a href="#">quite a few reports available</a> to analyse results. Especially the system wide reports which make use of hashtags are really helpful to find out what the users desire. And even if those system reports are insufficient, Tallymint supports custom reports!</p>
    </div>
    <div class="illustration" role="img" aria-label="Illustration of a large computer screen showing charts on a round island" style="left:531px;top:175px;width:168px;height:126px;background:linear-gradient(180deg,#e4e6ea 0%,#d9dde2 55%,var(--sky) 80%)"></div>

    <div class="illustration" role="img" aria-label="Illustration of white office buildings on a round island" style="left:15px;top:317px;width:170px;height:107px;background:linear-gradient(180deg,#eceef0 0%,#dfe2e5 55%,var(--sky) 82%)"></div>
    <div class="story" style="left:224px;top:318px;width:480px">
      <h2>Flexible analysis using <b>DQL</b></h2>
      <p>Tallymint introduces <a href="#">a draw query language (DQL)</a> which is more or less the same as SQL with an output solution. This language is easy to learn, and allows reading the users mind by just painting the data in fancy charts!</p>
    </div>
  </div>
</section>

<footer class="footer">
  <div class="wrap">
    <div class="brand">Tallymint</div>
    <div class="footer-col" style="left:0">
      <h3>Dokumentation</h3><div>Guides</div><div>Query Docs</div><div>Report Docs</div>
    </div>
    <div class="footer-col" style="left:75px">
      <h3>Information</h3><div>Ask Questions</div><div>Answer Questions</div><div>Official Blog</div>
    </div>
    <div class="footer-col" style="left:151px">
      <h3>About</h3><div>Privacy</div><div>Contact</div><div>About us</div>
    </div>
    <div class="social" aria-label="Social links"><span></span><span></span></div>
    <div class="copyright">© Tallymint, 2015</div>
  </div>
</footer>

</body>
</html>
```